QuarryNest - Webstartup looking for some style

QuarryNest is a cloud based web application that allows construction sub-contractors to create and manage bids. Generally, these contractors will contact subcontractors to have them do specific parts of a larger construction project. This would be used by various subcontractors including woodwork (cabinetry), electricians, masons, etc...

Nearly all competitors are clients applications that have to be installed on the computer and are very expensive. This is a much lower cost alternative.

The business is just beginning and we want people to view us as a fresh alternative to companies that have been around for a long time and are starting to look a little dated.

We would like our logo included on the card (see attached). We have been using the circular 'qn' emblem seperately from the complete logo in various areas of the website. We lean towards a professional and clean look, with a tendancy more towards modern.

We want to differentiate ourselves from our competition which tend to be dated, complicated and less graphical.

(We are currently designing our public website as well - but don't have any designs yet)

Industry/Entity Type

Construction

Requirements
Must have
• Circular 'qn' emblem from logo. Probably entire logo, but not necessarily.

Should have reference to website: www.quarrynest-demo.net

The Url should be all lowercase (www.quarrynest-demo.net)
Should not have
• we do not want to list a phone number or email address on the cards. we want people to go to the actual website. we haven't decided if we want names printed on the business cards.

```html
<!DOCTYPE html>
<html lang="en">
<head>
<meta charset="utf-8">
<title>QuarryNest Business Cards</title>
<link rel="stylesheet" href="https://fonts.googleapis.com/css2?family=Arimo:wght@400;700&display=swap">
<style>
  :root {
    --page-bg: #ffffff;
    --blue-light: #2aa9e2;
    --blue-mid: #1b8fd2;
    --blue-dark: #0d6cb4;
    --orange: #f7941d;
    --orange-light: #fbb040;
    --white: #ffffff;
    --ink-dark: #2b2b2b;
    --card-border: #d9d9d9;
  }
  * { margin: 0; padding: 0; box-sizing: border-box; }
  html, body {
    width: 1200px;
    height: 900px;
    overflow: hidden;
    background: var(--page-bg);
    font-family: "Arimo", Arial, sans-serif;
  }
  .canvas {
    position: relative;
    width: 1200px;
    height: 900px;
  }
  .card {
    position: absolute;
    width: 556px;
    height: 309px;
    border-radius: 18px;
    overflow: hidden;
    box-shadow: 2px 3px 5px rgba(0, 0, 0, 0.22);
  }
  .card-front {
    left: 320px;
    top: 125px;
    background: radial-gradient(ellipse 300px 230px at 50% 32%, var(--blue-light) 0%, var(--blue-light) 35%, var(--blue-mid) 70%, var(--blue-dark) 100%);
  }
  .card-back {
    left: 323px;
    top: 466px;
    background: var(--white);
    border: 1px solid var(--card-border);
  }
  .url-band {
    position: absolute;
    left: 0;
    right: 0;
    bottom: 0;
    height: 46px;
    display: flex;
    align-items: center;
    justify-content: center;
    color: var(--white);
    font-weight: 700;
    font-size: 20px;
    letter-spacing: 0.2px;
  }
  .url-band-orange {
    background: linear-gradient(90deg, var(--orange) 0%, var(--orange-light) 55%, var(--orange) 100%);
  }
  .url-band-blue {
    background: linear-gradient(90deg, var(--blue-dark) 0%, var(--blue-dark) 18%, var(--blue-light) 40%, var(--blue-light) 62%, var(--blue-dark) 84%, var(--blue-dark) 100%);
  }
  .front-mark {
    position: absolute;
    left: 0;
    right: 0;
    top: 92px;
    display: flex;
    flex-direction: column;
    align-items: center;
    gap: 10px;
  }
  .mark-dot {
    width: 72px;
    height: 72px;
    border-radius: 50%;
    background: var(--orange);
  }
  .front-name {
    color: var(--white);
    font-size: 24px;
    font-weight: 700;
  }
  .back-lockup {
    position: absolute;
    left: 0;
    right: 0;
    top: 122px;
    display: flex;
    align-items: center;
    justify-content: center;
    gap: 8px;
  }
  .lockup-dot {
    width: 50px;
    height: 50px;
    border-radius: 50%;
    background: var(--orange);
    flex: none;
  }
  .lockup-text {
    display: flex;
    flex-direction: column;
  }
  .back-name {
    color: var(--blue-dark);
    font-size: 34px;
    font-weight: 400;
    line-height: 1;
    letter-spacing: -0.5px;
  }
  .tagline {
    color: var(--ink-dark);
    font-size: 9.5px;
    font-weight: 700;
    margin-top: 3px;
    letter-spacing: -0.2px;
  }
</style>
</head>
<body>
  <main class="canvas">
    <section class="card card-front">
      <div class="front-mark">
        <div class="mark-dot"></div>
        <span class="front-name">QuarryNest</span>
      </div>
      <div class="url-band url-band-orange">www.quarrynest-demo.net</div>
    </section>

    <section class="card card-back">
      <div class="back-lockup">
        <div class="lockup-dot"></div>
        <div class="lockup-text">
          <span class="back-name">QuarryNest</span>
          <span class="tagline">Empowering Subcontractor Proposals</span>
        </div>
      </div>
      <div class="url-band url-band-blue">www.quarrynest-demo.net</div>
    </section>
  </main>
</body>
</html>
```